Need a flyer to leave behind when visiting clients or at shows

Glossy colorful tri-fold flyer with the same information that is on my web site www.brevalinkpro.com. I am open to a little modern or creative take on the typical brochure. I created the web site so I can provide any raw files needed from it. I would also like the ability to edit this flyer in the future in Adobe Photoshop Elements

```html
<!DOCTYPE html>
<html lang="en">
<head>
<meta charset="utf-8">
<title>BrevaLink Pro – Tri-fold Brochure</title>
<link href="https://fonts.googleapis.com/css2?family=Montserrat:wght@600;700;800&family=Open+Sans:ital,wght@0,400;0,600;1,400&display=swap" rel="stylesheet">
<style>
  :root{
    --sheet:#858585;
    --purple:#5a2a82;
    --purple-dark:#45196a;
    --white:#ffffff;
    --ink:#3a3a3a;
    --muted:#6f6f6f;
  }
  *{margin:0;padding:0;box-sizing:border-box}
  html,body{width:828px;height:1200px;overflow:hidden;background:var(--sheet)}
  body{position:relative;font-family:"Open Sans",Arial,sans-serif;color:var(--ink)}
  .side-label{position:absolute;left:14px;color:#e4e4e4;font:700 15px "Montserrat",Arial,sans-serif;letter-spacing:3px;writing-mode:vertical-rl;transform:rotate(180deg)}
  .spread{position:absolute;left:83px;width:739px;background:var(--white);box-shadow:0 4px 14px rgba(0,0,0,.35);overflow:hidden}
  .spread--outside{top:14px;height:541px}
  .spread--inside{top:625px;height:550px}
  .panel{position:absolute;top:0;bottom:0;width:246px;overflow:hidden}
  .panel:nth-child(1){left:0}.panel:nth-child(2){left:246px}.panel:nth-child(3){left:493px;width:246px}
  .photo{position:absolute}
  .band{position:absolute;left:0;right:0;background:var(--purple);color:var(--white)}
  h2{font:800 19px/1.15 "Montserrat",Arial,sans-serif;text-transform:uppercase}
  h3{font:700 13px "Montserrat",Arial,sans-serif;text-transform:uppercase;color:var(--purple)}
  .objective{text-align:center;margin-top:18px}
  .objective p{font:700 10.5px/1.3 "Montserrat",Arial,sans-serif;text-transform:uppercase}
  .icon{display:block;margin:0 auto 6px}
  .brand{display:inline-flex;align-items:center;gap:6px;background:var(--purple);color:var(--white);font:700 18px "Montserrat",Arial,sans-serif;padding:8px 12px}
  .brand i{width:10px;height:10px;background:var(--white);display:block}
  .contact li{list-style:none;font-size:11px;margin:6px 0;display:flex;align-items:center;gap:7px}
  .body-text{font-size:8.5px;line-height:1.45;color:var(--muted)}
  .values{display:flex;flex-direction:column;align-items:center;gap:10px}
  .value{display:flex;flex-direction:column;align-items:center;width:100%}
  .value p{font:700 8.5px "Montserrat",Arial,sans-serif;text-transform:uppercase;text-align:center;margin-top:4px}
  .value-icon{width:30px;height:30px;background:var(--white);display:flex;align-items:center;justify-content:center}
  .service-list li{list-style:none;font-size:9.5px;margin:7px 0;padding-left:14px;position:relative}
  .service-list li::before{content:"";position:absolute;left:0;top:4px;width:6px;height:6px;background:var(--white)}
</style>
</head>
<body>

<div class="side-label" style="top:40px">FRONT/BACK</div>
<div class="side-label" style="top:660px">INSIDE</div>

<section class="spread spread--outside">
  <div class="panel objectives">
    <div class="photo" role="img" aria-label="Hands touching a digital hexagon interface" style="top:0;left:0;right:0;height:150px;background:linear-gradient(135deg,#c8d4de,#f2f5f8)"></div>
    <div class="band" style="top:150px;bottom:0;padding:24px 20px;text-align:center">
      <h2>Our Primary<br>Objectives</h2>
      <div class="objective">
        <svg class="icon" width="34" height="34" viewBox="0 0 34 34"><circle cx="17" cy="17" r="15" fill="none" stroke="#fff" stroke-width="2"/><path d="M10 17l5 5 9-10" fill="none" stroke="#fff" stroke-width="2.5"/></svg>
        <p>Understand and exceed<br>client expectations</p>
      </div>
      <div class="objective">
        <svg class="icon" width="34" height="34" viewBox="0 0 34 34"><circle cx="17" cy="17" r="15" fill="none" stroke="#fff" stroke-width="2"/><path d="M8 18l6-5 5 4 7-5M12 20l5 4 6-4" fill="none" stroke="#fff" stroke-width="2"/></svg>
        <p>Committed to be a partner,<br>not vendor</p>
      </div>
      <div class="objective">
        <svg class="icon" width="34" height="34" viewBox="0 0 34 34"><circle cx="17" cy="17" r="15" fill="none" stroke="#fff" stroke-width="2"/><circle cx="17" cy="17" r="5" fill="none" stroke="#fff" stroke-width="2"/><path d="M17 8v4M17 22v4M8 17h4M22 17h4" stroke="#fff" stroke-width="2"/></svg>
        <p>Provide simplified change<br>management expertise</p>
      </div>
    </div>
  </div>

  <div class="panel mailer">
    <p style="position:absolute;top:16px;left:20px;right:14px;font-style:italic;font-size:12.5px;line-height:1.35;color:var(--purple)">Providing<br>information technology<br>expertise to post-acute<br>care providers</p>
    <div class="photo" role="img" aria-label="Professional working with a tablet" style="top:100px;left:0;right:0;height:230px;background:linear-gradient(160deg,#6e7f8f,#c9d2da)"></div>
    <div class="band" style="top:330px;bottom:0;padding:26px 20px">
      <span class="brand" style="font-size:15px;background:var(--purple-dark)"><i></i>BrevaLink Pro</span>
      <ul class="contact" style="margin-top:26px">
        <li><svg width="12" height="12" viewBox="0 0 12 12"><path d="M2 1h3l1 3-2 1a7 7 0 0 0 3 3l1-2 3 1v3c-6 1-10-3-9-9z" fill="#fff"/></svg>555-010-2082</li>
        <li><svg width="12" height="12" viewBox="0 0 12 12"><circle cx="6" cy="6" r="5" fill="none" stroke="#fff" stroke-width="1.5"/><path d="M1 6h10M6 1v10" stroke="#fff"/></svg>www.brevalinkpro.com</li>
        <li><svg width="12" height="12" viewBox="0 0 12 12"><rect x="1" y="2.5" width="10" height="7" fill="none" stroke="#fff" stroke-width="1.3"/><path d="M1 3l5 4 5-4" fill="none" stroke="#fff" stroke-width="1.3"/></svg>hello@brevalinkpro.com</li>
      </ul>
    </div>
  </div>

  <div class="panel cover">
    <div class="photo" role="img" aria-label="Collage of healthcare and technology photos" style="top:0;left:0;right:0;height:330px;background:linear-gradient(135deg,#b4c3d0,#eef2f5)"></div>
    <div style="position:absolute;top:18px;right:18px"><span class="brand" style="font-size:20px;padding:12px 14px"><i></i>BrevaLink Pro</span></div>
    <div class="band" style="top:330px;bottom:0;padding:40px 22px;text-align:center">
      <h2 style="font-size:17px;line-height:1.3">Increasing the value and security of your technology resources</h2>
    </div>
  </div>
</section>

<section class="spread spread--inside">
  <div class="panel about" style="padding:18px 18px">
    <h3>About Us</h3>
    <p class="body-text" style="margin-top:4px"><b>Our Mission:</b> Partner with clients to increase the value and security of their technology tools.</p>
    <p class="body-text" style="margin-top:4px"><b>Our Goal:</b> Become the premier consulting company for information technology in the post-acute care community.</p>
    <p class="body-text" style="margin-top:6px">Founded by experts in post-acute and IT fields, we bring decades of hands-on experience in planning, security and support for care providers of every size, helping teams work better every day.</p>
    <h3 style="margin-top:12px">Our Leaders</h3>
    <div class="photo" role="img" aria-label="Portrait of company leader" style="top:205px;left:18px;width:58px;height:68px;background:linear-gradient(180deg,#b9a99c,#e9e2dc)"></div>
    <p class="body-text" style="position:absolute;top:205px;left:84px;right:18px">Dana Reyes, Founder, leads every client project with a focus on service, trust and clear results.</p>
    <div class="photo" role="img" aria-label="Team meeting around a laptop" style="top:300px;left:0;right:0;bottom:0;background:linear-gradient(150deg,#8f7d70,#e2d8cf)"></div>
  </div>

  <div class="panel core-values">
    <div class="photo" role="img" aria-label="Colleagues collaborating at a desk" style="top:0;left:0;right:0;height:225px;background:linear-gradient(150deg,#7c8a96,#dfe3e6)"></div>
    <div class="band" style="top:225px;bottom:0;padding:20px 16px;background:linear-gradient(180deg,var(--purple),var(--purple-dark))">
      <h2 style="text-align:center;font-size:15px;margin-bottom:14px">Our Core Values</h2>
      <div class="values">
        <div class="value"><div class="value-icon"><svg width="18" height="18" viewBox="0 0 18 18"><circle cx="9" cy="6" r="3.5" fill="#5a2a82"/><path d="M2 17c1-5 13-5 14 0z" fill="#5a2a82"/></svg></div><p>Client Focused</p></div>
        <div class="value"><div class="value-icon"><svg width="18" height="18" viewBox="0 0 18 18"><path d="M3 9l4 4 8-9" fill="none" stroke="#5a2a82" stroke-width="2.5"/></svg></div><p>Accountability</p></div>
        <div class="value"><div class="value-icon"><svg width="18" height="18" viewBox="0 0 18 18"><path d="M9 1l7 3v5c0 4-3 7-7 8-4-1-7-4-7-8V4z" fill="#5a2a82"/></svg></div><p>Integrity</p></div>
        <div class="value"><div class="value-icon"><svg width="18" height="18" viewBox="0 0 18 18"><path d="M2 15h3V9H2zM7.5 15h3V5h-3zM13 15h3V2h-3z" fill="#5a2a82"/></svg></div><p>Professional Development</p></div>
      </div>
    </div>
  </div>

  <div class="panel services" style="padding:18px 18px">
    <h3>Our Services</h3>
    <p class="body-text" style="margin-top:5px">We understand the unique needs of care providers and tailor each service to protect data, support staff and keep every system running smoothly.</p>
    <div class="photo" role="img" aria-label="Digital IT technology concept graphic" style="top:92px;left:0;right:0;height:150px;background:linear-gradient(135deg,#3f6fa8,#b7d3ee)"></div>
    <div class="band" style="top:250px;bottom:0;padding:18px 18px">
      <h2 style="font-size:13px">Information Technology</h2>
      <ul class="service-list" style="margin-top:10px">
        <li>CIO or IT Director Services</li>
        <li>CISO or Information Security Officer</li>
        <li>Comprehensive HIPAA Risk Assessments</li>
        <li>IT Department Evaluation</li>
        <li>Policy Management and Consulting</li>
        <li>On-going IT department support</li>
      </ul>
    </div>
  </div>
</section>

</body>
</html>
```